Quellmont Haus National Website

We need a website to match our Logo. We will be selling american made vapeing Oils, batteries, Cartomizers, Clearomizers. We have a wharehouse location with couches, TVs streaming clipora, vending machine, and the worlds first flavor mixing bar. We have the lowest priced high grade oils. We will send pictures of the location. Relaxed atmoshpere and no lines for purchase. VIP cards for regulars.

(PLEASE KNOW THAT THE LOGO IS THE UPPER RIGHT LOGO ONLY OF THE FOUR ON THE FILE I ATTACHED)
Updates

Keep in mind we are are only looking for concept and a non coded website

Please know that we are looking for a non coded website

Industry/Entity Type

Purchase

Requirements
Must have
• Online cart, Blog,

```html
<!DOCTYPE html>
<html lang="en">
<head>
<meta charset="utf-8">
<title>Quellmont Haus</title>
<link href="https://fonts.googleapis.com/css2?family=Arimo:wght@400;700&family=PT+Sans:wght@400;700&display=swap" rel="stylesheet">
<style>
:root{
  --green:#8cc63f;
  --dark:#1f1f1f;
  --bar:rgba(52,58,56,.82);
  --cream:#f2f0ea;
  --text:#333;
  --red:#c8322a;
  --white:#fff;
}
*{margin:0;padding:0;box-sizing:border-box}
html,body{width:1200px;height:1071px;overflow:hidden}
body{font-family:"Arimo",Arial,sans-serif;background:var(--cream);position:relative}
.hero{position:absolute;left:0;top:0;width:1200px;height:550px;overflow:hidden;
  background:
    radial-gradient(ellipse 260px 300px at 1000px 260px,rgba(196,150,130,.85),rgba(196,150,130,0) 70%),
    radial-gradient(ellipse 220px 160px at 880px 380px,rgba(220,225,240,.7),rgba(220,225,240,0) 75%),
    radial-gradient(ellipse 300px 220px at 480px 220px,rgba(230,170,220,.75),rgba(230,170,220,0) 75%),
    radial-gradient(ellipse 180px 200px at 320px 170px,rgba(255,215,170,.55),rgba(255,215,170,0) 75%),
    radial-gradient(ellipse 200px 320px at 70px 320px,rgba(170,150,150,.8),rgba(170,150,150,0) 75%),
    radial-gradient(ellipse 500px 180px at 600px 520px,rgba(90,120,190,.8),rgba(90,120,190,0) 75%),
    linear-gradient(90deg,#4a4a6e,#6b5c86 35%,#3f4f7a 70%,#26304e)}
.hero-photo{position:absolute;inset:0}
.topbar{position:absolute;left:0;top:0;width:1200px;height:94px;background:var(--bar);border-bottom:1px solid rgba(255,255,255,.12)}
.logo{position:absolute;left:160px;top:13px;font-size:26px;color:var(--green);font-weight:400}
.welcome{position:absolute;left:551px;top:11px;font-size:11px;color:var(--white)}
.sep{position:absolute;left:822px;top:10px;width:1px;height:13px;background:#ccc}
.cart{position:absolute;left:840px;top:8px;display:flex;align-items:center;gap:6px;font-size:11px;color:var(--white);font-weight:700}
.cart .count{color:var(--green);margin-left:8px}
.nav{position:absolute;left:0;top:61px;width:1200px;font-size:11.5px;font-weight:700;color:var(--white)}
.nav span{position:absolute;white-space:nowrap}
.search{position:absolute;left:866px;top:53px;width:199px;height:26px;border:1px solid #bbb;color:var(--white);font-size:12px;padding:5px 8px}
.search svg{position:absolute;right:6px;top:5px}
.search::after{content:"";position:absolute;right:28px;top:3px;width:1px;height:18px;background:#888}
.caption{position:absolute;left:149px;background:rgba(40,40,40,.85);color:#f4f1ea;font-weight:700;white-space:nowrap}
.cap1{top:355px;width:646px;height:52px;font-size:37.5px;padding:4px 12px}
.cap2{top:414px;width:539px;height:52px;font-size:22.5px;padding:14px 12px}
.arrow{position:absolute;top:478px;width:39px;height:38px;background:var(--green);display:flex;align-items:center;justify-content:center}
.strip{position:absolute;left:0;top:550px;width:1200px;height:160px;background:var(--dark);border-bottom:2px dashed #444}
.thumb{position:absolute;top:31px;width:204px;height:94px}
.thumb.active{top:29px;left:157px;width:209px;height:98px;border:3px solid var(--green)}
.arrivals{position:absolute;left:150px;top:745px;width:900px;text-align:center}
.arrivals::before{content:"";position:absolute;left:0;right:0;top:15px;height:1px;background:#ccc}
.arrivals h2{position:relative;display:inline-block;background:var(--cream);padding:0 14px;font-size:22px;font-weight:400;color:#333}
.product{position:absolute;top:798px;width:205px;text-align:center;font-family:"PT Sans",sans-serif}
.product .img{height:148px;background:#fff}
.product .name{margin-top:15px;font-size:13px;color:#444}
.product .price{margin-top:3px;font-size:11.5px;font-weight:700;color:#222}
.product .btn{display:inline-block;margin-top:8px;background:var(--red);color:#fff;font-size:9.5px;font-weight:700;padding:4px 9px;border:1px solid #8e1d18}
</style>
</head>
<body>
<section class="hero">
  <div class="hero-photo" role="img" aria-label="Customer exhaling vapor at a lounge bar with glowing bottles behind"></div>
  <header class="topbar">
    <div class="logo">Quellmont Haus</div>
    <div class="welcome">Welcome visitor you can login or create an account</div>
    <div class="sep"></div>
    <div class="cart">
      <svg width="20" height="18" viewBox="0 0 20 18"><path d="M1 2h3l3 9h9l2-6H6" fill="none" stroke="#fff" stroke-width="2"/><circle cx="8" cy="15" r="1.6" fill="#fff"/><circle cx="15" cy="15" r="1.6" fill="#fff"/></svg>
      Shopping Cart <span class="count">( 1 item - $60.00 )</span>
      <svg width="10" height="8" style="margin-left:8px"><path d="M0 1h10L5 7z" fill="#ccc"/></svg>
    </div>
    <nav class="nav">
      <span style="left:158px">Home</span><span style="left:220px">Flavor Collections</span><span style="left:351px">Carto/Clearo-mizer</span><span style="left:491px">Battery</span><span style="left:560px">Others</span><span style="left:637px">Location</span><span style="left:714px">Blog</span><span style="left:769px">Contact</span>
    </nav>
    <div class="search">Search...
      <svg width="14" height="14" viewBox="0 0 14 14"><circle cx="8" cy="6" r="4" fill="none" stroke="#fff" stroke-width="1.5"/><path d="M5 9l-4 4" stroke="#fff" stroke-width="1.5"/></svg>
    </div>
  </header>
  <div class="caption cap1">The first Vapor Oil Flavor Mix Bar</div>
  <div class="caption cap2">Try, and exprience new flavor, mix it your own !</div>
  <div class="arrow" style="left:149px"><svg width="12" height="14"><path d="M9 2L3 7l6 5" fill="none" stroke="#fff" stroke-width="3"/></svg></div>
  <div class="arrow" style="left:194px"><svg width="12" height="14"><path d="M3 2l6 5-6 5" fill="none" stroke="#fff" stroke-width="3"/></svg></div>
</section>
<section class="strip">
  <div class="thumb active" style="background:radial-gradient(ellipse 50px 40px at 150px 50px,#c9a79a,transparent 80%),radial-gradient(ellipse 60px 40px at 90px 30px,#d8a0c8,transparent 80%),linear-gradient(90deg,#5d4f70,#4a5f8c)" role="img" aria-label="Vapor bar scene"></div>
  <div class="thumb" style="left:384px;background:radial-gradient(ellipse 40px 22px at 100px 30px,#3a3a3a,transparent 90%),linear-gradient(180deg,#f2efec 45%,#e2d6c6 70%,#b8a58c)" role="img" aria-label="Lounge couch facing a TV"></div>
  <div class="thumb" style="left:609px;background:radial-gradient(ellipse 40px 40px at 130px 35px,#d9c2a8,transparent 85%),radial-gradient(ellipse 40px 40px at 60px 40px,#c29a7c,transparent 85%),linear-gradient(180deg,#6a5646,#3a2e28)" role="img" aria-label="Friends relaxing together"></div>
  <div class="thumb" style="left:836px;background:radial-gradient(ellipse 30px 50px at 180px 60px,#1f8a7c,transparent 90%),radial-gradient(ellipse 20px 50px at 65px 60px,#2e3a2a,transparent 90%),linear-gradient(180deg,#f4f4f4,#cfcfcf)" role="img" aria-label="Vapor batteries and tanks on display"></div>
</section>
<div class="arrivals"><h2>New Arrivals</h2></div>
<div class="product" style="left:159px"><div class="img" role="img" aria-label="Portable vaporizers in colorful boxes" style="background:radial-gradient(ellipse 80px 60px at 100px 70px,#4a4a4e,rgba(74,74,78,.3) 60%,#fff 100%)"></div><div class="name">Ardent Portable Vaporizers</div><div class="price">$119.50 $107.75</div><span class="btn">ADD TO CART</span></div>
<div class="product" style="left:384px"><div class="img" role="img" aria-label="Desktop vaporizer set with accessories" style="background:radial-gradient(ellipse 40px 30px at 40px 40px,#e8903a,transparent 90%),radial-gradient(ellipse 80px 50px at 120px 95px,#b8bcc2,#fff 100%)"></div><div class="name">Cinder Classics Set</div><div class="price">$119.50 $107.75</div><span class="btn">ADD TO CART</span></div>
<div class="product" style="left:610px"><div class="img" role="img" aria-label="Handheld black vaporizer" style="background:radial-gradient(ellipse 55px 50px at 100px 80px,#2a2a2a,rgba(60,60,60,.35) 65%,#fff 100%)"></div><div class="name">Halvo ONE Vaporizer</div><div class="price">$119.50 $107.75</div><span class="btn">ADD TO CART</span></div>
<div class="product" style="left:836px"><div class="img" role="img" aria-label="Vaporizer with blue box packaging" style="background:radial-gradient(ellipse 30px 55px at 50px 90px,#3a3030,transparent 90%),radial-gradient(ellipse 70px 50px at 140px 80px,#2f5fa8,rgba(47,95,168,.3) 70%,#fff 100%)"></div><div class="name">Bountiful Vapor Set</div><div class="price">$119.50 $107.75</div><span class="btn">ADD TO CART</span></div>
</body>
</html>
```